LunaForm Informational Flyer Design

Hello, we are a team of two who opened an all women's gym located in Seattle, WA. We've been in business for four and a half years renting from various other facilities such as crossfit, a banquet hall, and outside at local parks, and opened our own facility in January 2016.
Check www.lunaformstudio-example.com for more info about our gym, our team, and what we offer to our clients.
We are looking for a strong, clean, but feminine double-sided leaflet or something a little larger than the average postcard to pass out to local businesses, schools and other charitable auctions, and neighboring apartment buildings that are currently under construction. DL size
We have more images should you need them for the design, some more abstract of just equipment; included a few here along with our logo.
Please let me know if you need more info or more pics.
Thanks in advance!

Hello, I have updated the brief with more specifics. Please take a look and resubmit with thanks. Added Thursday, February 16, 2017

Target Market(s)

Women ages 18-70

Industry/Entity Type

Fitness

Font styles to use
Other font styles liked:
• Futura (SEE NOTES)

Colors
e34197
000000

Requirements
Must have
• DL Size
• Front should be clean and simple and include:
• • LOGO
• • RESULTS-DRIVEN WOMEN’S FITNESS
• • FREE INTRODUCTORY WEEK
• • pictures of LUNAPULSE, LUNAPOISE, & LUNAFLOW with names overlaid on pictures (see home page of website)
• ◦ *CHILDCARE INCLUDED (underneath program pictures, but not too big)
• BACK side:
• • LunaForm is not just a women's gym. We are a community of women grinding and growing into the very best versions of ourselves.  LunaForm’s mission is simple -- to get you strong, balanced, and flexible for life both in and out of the gym.
• • PROGRAMS:   (Optional to include pictures of each program)
• LUNAPULSE underneath should list ASCEND & LUNAFIRST
• LUNAPOISE
• LUNAFLOW underneath should list LUNA STRONG STREAM & RESTORATIVE YOGA
• • PRICING (includes childcare)
• ANNUAL $1675
• MONTHLY $159
• 10 CLASS PASS $199
• DROP-IN $25
• *See website for special discounts*
• • Phone
• • Email
• • Address
• • Website
• • COUPON CODE section with some space underneath to handwrite in a coupon code. 
Nice to have
• If it works with the design and doesn't make it too cluttered, instead of FREE INTRODUCTORY WEEK on front side, can say CLAIM YOUR FREE INTRO WEEK HERE (or some other wording) and include a QR code that goes directly to our scheduling site: https://lunaform.bookdeskapp-example.com/welcome
• Can use the fonts in the logo or designer preference on what will work best with design.

```html
<!DOCTYPE html>
<html lang="en">
<head>
<meta charset="utf-8">
<title>LunaForm Flyer</title>
<link rel="stylesheet" href="https://fonts.googleapis.com/css2?family=Rajdhani:wght@600;700&family=Roboto+Condensed:wght@700&family=Lato:wght@400;700&display=swap">
<style>
  :root {
    --magenta: #e32c9b;
    --magenta-deep: #c81f86;
    --black: #000000;
    --ink: #1c1c1c;
    --white: #ffffff;
    --page: #ececec;
  }
  * { box-sizing: border-box; margin: 0; padding: 0; }
  html, body { width: 1200px; height: 1200px; overflow: hidden; background: var(--page); }
  .canvas { position: relative; width: 1200px; height: 1200px; }
  .flyer { position: absolute; top: 218px; width: 534px; height: 766px; overflow: hidden; background: var(--white); }
  .flyer--front { left: 53px; }
  .flyer--back { left: 616px; background: var(--magenta); }
  .layer { position: absolute; left: 0; top: 0; width: 534px; height: 766px; }

  /* front */
  .hero-photo { position: absolute; left: 0; top: 0; width: 534px; height: 490px;
    background: linear-gradient(135deg, #b8449c 0%, var(--magenta) 45%, #e0409c 70%, #c93a8e 100%); }
  .brand { position: absolute; left: 0; width: 534px; text-align: center; color: var(--white); }
  .brand__name { top: 36px; font: 700 58px/1 "Rajdhani", sans-serif; letter-spacing: 3px; }
  .brand__tagline { top: 98px; font: 600 23px/1 "Rajdhani", sans-serif; letter-spacing: 3px; }
  .headline { position: absolute; color: var(--white); font: 700 48px/1 "Roboto Condensed", sans-serif;
    text-shadow: 0 2px 6px rgba(0,0,0,.35); white-space: nowrap; }
  .headline--1 { left: 86px; top: 236px; }
  .headline--2 { left: 106px; top: 276px; }
  .headline--3 { left: 259px; top: 316px; }
  .services-title { position: absolute; top: 493px; left: 0; width: 534px; display: flex; justify-content: center;
    align-items: center; gap: 8px; color: var(--magenta); font: 700 19px/1 "Rajdhani", sans-serif; }
  .services { position: absolute; top: 533px; left: 54px; display: flex; gap: 30px; }
  .service { position: relative; width: 122px; height: 122px; border-radius: 50%;
    background: radial-gradient(circle at 40% 35%, #6a6a6a, #2c2c2c 70%);
    display: flex; align-items: center; justify-content: center; }
  .service__name { color: var(--white); font: 700 17px/1 "Lato", sans-serif; }
  .contact { position: absolute; left: 55px; color: var(--ink); font: 400 14px/1 "Lato", sans-serif;
    display: flex; align-items: center; gap: 8px; white-space: nowrap; }
  .contact--phone { top: 676px; font: 700 17px/1 "Lato", sans-serif; }
  .contact--email { top: 678px; left: 205px; }
  .contact--address { top: 704px; }
  .contact--web { top: 731px; }
  .contact svg { flex: none; }
  .front-art { position: absolute; left: 380px; top: 702px; width: 124px; height: 64px;
    border-radius: 40px 40px 0 0;
    background: linear-gradient(180deg, rgba(227,44,155,.55), var(--magenta)); }

  /* back */
  .section-title { position: absolute; left: 47px; top: 48px; color: var(--white); font: 700 29px/1 "Rajdhani", sans-serif; }
  .community-copy { position: absolute; left: 47px; top: 87px; width: 400px; color: var(--white);
    font: 400 12.6px/15.4px "Lato", sans-serif; }
  .together { position: absolute; left: 47px; top: 212px; color: var(--white); font: 600 23px/23px "Rajdhani", sans-serif; }
  .back-art { position: absolute; left: 345px; top: 198px; width: 170px; height: 140px;
    border-radius: 60px 60px 20px 20px;
    background: linear-gradient(180deg, rgba(255,255,255,.35), rgba(255,255,255,.75)); }
  .offer { position: absolute; right: 32px; top: 404px; text-align: right; color: var(--white);
    font: 700 45px/40px "Rajdhani", sans-serif; }
  .childcare { position: absolute; right: 32px; top: 539px; color: var(--white); font: 400 15px/1 "Lato", sans-serif; }
  .coupon { position: absolute; left: 278px; top: 594px; width: 256px; height: 126px; background: var(--white);
    border-radius: 8px 0 0 8px; }
  .coupon__label { display: block; text-align: center; padding-top: 12px; color: var(--ink);
    font: 700 21px/1 "Rajdhani", sans-serif; }
</style>
</head>
<body>
<main class="canvas">

  <section class="flyer flyer--front">
    <div class="hero-photo" role="img" aria-label="Photo of the two studio founders standing arms crossed in a pink-lit gym"></div>
    <svg class="layer" viewBox="0 0 534 766" aria-hidden="true">
      <path d="M0,472 C160,446 360,412 534,424 L534,766 L0,766 Z" fill="#ffffff"/>
      <path d="M0,468 C160,442 360,408 534,420" fill="none" stroke="#e32c9b" stroke-width="5"/>
    </svg>

    <div class="brand brand__name">LUNAFORM</div>
    <div class="brand brand__tagline">YOU WILL ASCEND</div>

    <h1>
      <span class="headline headline--1">RESULTS</span>
      <span class="headline headline--2">DRIVEN WOMEN'S</span>
      <span class="headline headline--3">FITNESS</span>
    </h1>

    <h2 class="services-title">
      <svg width="38" height="18" viewBox="0 0 38 18" aria-hidden="true"><g fill="#1c1c1c"><rect x="0" y="6" width="3" height="6"/><rect x="4" y="2" width="4" height="14"/><rect x="9" y="0" width="3" height="18"/><rect x="12" y="8" width="26" height="3"/></g></svg>
      SERVICES OFFERED
      <svg width="38" height="18" viewBox="0 0 38 18" aria-hidden="true"><g fill="#1c1c1c"><rect x="0" y="8" width="26" height="3"/><rect x="26" y="0" width="3" height="18"/><rect x="30" y="2" width="4" height="14"/><rect x="35" y="6" width="3" height="6"/></g></svg>
    </h2>

    <div class="services">
      <div class="service" role="img" aria-label="Photo of a high intensity interval class"><span class="service__name">LUNAPULSE</span></div>
      <div class="service" role="img" aria-label="Photo of a barre class"><span class="service__name">LUNAPOISE</span></div>
      <div class="service" role="img" aria-label="Photo of a yoga class"><span class="service__name">LUNAFLOW</span></div>
    </div>

    <div class="front-art" role="img" aria-label="Pink silhouette illustration of women lifting weights"></div>

    <div class="contact contact--phone">
      <svg width="13" height="20" viewBox="0 0 13 20" aria-hidden="true"><rect x="1" y="1" width="11" height="18" rx="2" fill="none" stroke="#e32c9b" stroke-width="1.8"/><rect x="5" y="15" width="3" height="1.6" fill="#e32c9b"/></svg>
      206.555.0142
    </div>
    <div class="contact contact--email">
      <svg width="16" height="11" viewBox="0 0 16 11" aria-hidden="true"><rect x="0" y="0" width="16" height="11" fill="#e32c9b"/><path d="M0,0 L8,6 L16,0" fill="none" stroke="#fff" stroke-width="1.4"/></svg>
      hello@lunaformstudio-example.com
    </div>
    <div class="contact contact--address">
      <svg width="14" height="19" viewBox="0 0 14 19" aria-hidden="true"><path d="M7,1 C3.5,1 1,3.6 1,7 C1,11 7,17 7,17 C7,17 13,11 13,7 C13,3.6 10.5,1 7,1 Z" fill="#e32c9b"/><circle cx="7" cy="7" r="2.3" fill="#fff"/></svg>
      1270 Harbor Crest Ave SW Seattle, WA 98199
    </div>
    <div class="contact contact--web">
      <svg width="16" height="16" viewBox="0 0 16 16" aria-hidden="true"><g fill="none" stroke="#e32c9b" stroke-width="1.2"><circle cx="8" cy="8" r="7"/><ellipse cx="8" cy="8" rx="3" ry="7"/><line x1="1" y1="8" x2="15" y2="8"/></g></svg>
      www.lunaformstudio-example.com
    </div>
  </section>

  <section class="flyer flyer--back">
    <h2 class="section-title">OUR COMMUNITY</h2>
    <p class="community-copy">Our clients are amazed at the mental and physical transformations that come from training in our crew of welcoming and empowering women.&nbsp; No matter if you're just starting your fitness journey or how advanced your skills may be, you will feel inspired and engaged the minute you step through the door.&nbsp; Friendships and trust form here, and at the end of every sweat-drenched booty kicking, you'll love our cool down, reflection, and gratitude section.</p>
    <p class="together">WE'RE ON THIS<br>JOURNEY TOGETHER!</p>

    <div class="back-art" role="img" aria-label="White silhouette illustration of women training with kettlebell and barbell"></div>

    <svg class="layer" viewBox="0 0 534 766" role="img" aria-label="Moody photo of an athletic woman in a black sports top">
      <defs>
        <linearGradient id="athletePhoto" x1="0" y1="0" x2="1" y2="1">
          <stop offset="0" stop-color="#1a1614"/>
          <stop offset="0.35" stop-color="#5a4438"/>
          <stop offset="0.6" stop-color="#1d1817"/>
          <stop offset="1" stop-color="#050505"/>
        </linearGradient>
      </defs>
      <path d="M0,294 C150,298 320,352 420,346 C470,343 505,332 534,330 L534,766 L0,766 Z" fill="url(#athletePhoto)"/>
      <path d="M0,294 C150,298 320,352 420,346 C470,343 505,332 534,330" fill="none" stroke="#ffffff" stroke-width="4"/>
    </svg>

    <h1 class="offer">CLAIM YOUR<br>FREE INTRO<br>WEEK HERE</h1>
    <p class="childcare">Childcare service available</p>

    <div class="coupon">
      <span class="coupon__label">USE COUPON CODE</span>
    </div>
  </section>

</main>
</body>
</html>
```